A comunicação apenas pelo chat ou com desenvolvedor que não se comunica com cliente é péssimo ! O desenvolvedor que não se comunica dificulta o desenvolvimento do trabalho causando uma demora ecessiva !

```html
<!DOCTYPE html>
<html lang="pt-BR">
<head>
<meta charset="utf-8">
<title>Obra Plena Projetos – Envelope</title>
<link rel="stylesheet" href="https://fonts.googleapis.com/css2?family=Montserrat:wght@500&display=swap">
<style>
  :root {
    --backdrop: #e6e7e8;
    --paper: #ffffff;
    --ink: #1a1a1a;
    --ink-soft: #3a3a3a;
  }
  * { margin: 0; padding: 0; box-sizing: border-box; }
  html, body { width: 1200px; height: 1200px; overflow: hidden; background: var(--backdrop); }
  .canvas {
    position: relative;
    width: 1200px;
    height: 1200px;
    overflow: hidden;
    background: var(--backdrop);
    font-family: "Montserrat", Arial, sans-serif;
    color: var(--ink);
  }
  .dieline { position: absolute; inset: 0; width: 1200px; height: 1200px; }
  .dieline path { fill: var(--paper); }

  .brand {
    position: absolute;
    display: flex;
    align-items: center;
    gap: 14px;
  }
  .brand__square { width: 40px; height: 40px; background: var(--ink); flex: none; }
  .brand__name {
    font-weight: 500;
    font-size: 22px;
    line-height: 1.18;
    letter-spacing: 0.09em;
    text-transform: uppercase;
    border-left: 2px solid var(--ink);
    padding-left: 10px;
  }
  .brand--flap { left: 233px; top: 405px; }
  .brand--front {
    left: 520px; top: 676px;
    transform: rotate(180deg);
    transform-origin: center;
  }

  .contacts {
    position: absolute;
    left: 410px; top: 546px;
    width: 324px;
    transform: rotate(180deg);
    transform-origin: center;
    font-size: 10.5px;
    font-weight: 500;
    color: var(--ink-soft);
    display: grid;
    grid-template-columns: auto auto;
    column-gap: 30px;
    row-gap: 6px;
    justify-content: center;
  }
  .contacts__item { display: flex; align-items: center; gap: 6px; white-space: nowrap; }
  .contacts__item svg { width: 11px; height: 11px; flex: none; }
  .contacts__item--address { grid-column: 1 / -1; justify-content: center; }
</style>
</head>
<body>
<main class="canvas">
  <svg class="dieline" viewBox="0 0 500 500" aria-hidden="true">
    <path d="M98 42 H402 Q418 42 420 58 L438 205 Q440 216 445 217 V362 Q440 363 438 372 L420 442 Q418 458 402 458 H98 Q82 458 80 442 L62 372 Q60 363 55 362 V217 Q60 216 62 205 L80 58 Q82 42 98 42 Z"/>
  </svg>

  <div class="brand brand--flap">
    <span class="brand__square"></span>
    <span class="brand__name">Obra Plena<br>Projetos</span>
  </div>

  <div class="contacts">
    <span class="contacts__item">
      <svg viewBox="0 0 12 12"><circle cx="6" cy="6" r="5.5" fill="none" stroke="currentColor"/><path d="M4 3.2 L5 4.6 L4.5 5.3 Q5.4 6.8 6.7 7.5 L7.4 7 L8.8 8 L8 9 Q5 8.5 3.2 4 Z" fill="currentColor"/></svg>
      +55 31 4000-2716 • +55 31 4000-2717
    </span>
    <span class="contacts__item">
      <svg viewBox="0 0 12 12"><rect x="1" y="2.5" width="10" height="7" fill="currentColor"/><path d="M1 2.5 L6 6.5 L11 2.5" fill="none" stroke="#fff" stroke-width="0.8"/></svg>
      ola@obraplena.com.br
    </span>
    <span class="contacts__item">
      <svg viewBox="0 0 12 12"><circle cx="6" cy="6" r="5.5" fill="none" stroke="currentColor"/><path d="M4 3.2 L5 4.6 L4.5 5.3 Q5.4 6.8 6.7 7.5 L7.4 7 L8.8 8 L8 9 Q5 8.5 3.2 4 Z" fill="currentColor"/></svg>
      +55 31 4000-2716
    </span>
    <span class="contacts__item">
      <svg viewBox="0 0 12 12"><circle cx="6" cy="6" r="5" fill="none" stroke="currentColor"/><path d="M1 6 H11 M6 1 Q3 6 6 11 M6 1 Q9 6 6 11" fill="none" stroke="currentColor" stroke-width="0.7"/></svg>
      www.obraplena.com.br
    </span>
    <span class="contacts__item contacts__item--address">
      <svg viewBox="0 0 12 12"><path d="M6 11 Q2 6.5 2 4.5 A4 4 0 0 1 10 4.5 Q10 6.5 6 11 Z" fill="currentColor"/><circle cx="6" cy="4.5" r="1.4" fill="#fff"/></svg>
      Endereço: Rua Modelo - N 42
    </span>
  </div>

  <div class="brand brand--front">
    <span class="brand__square"></span>
    <span class="brand__name">Obra Plena<br>Projetos</span>
  </div>
</main>
</body>
</html>
```